Vandrel Design Project

Hello,
I need a general vandrel background design for a new webpage.
Reason: We did close the site until September 1st to fix some development issues.
The design we have received so far are ok, but not yet what I am looking for.
You can contact me directly at mdravek (at) fennomail.com if you have any questions I may help you with.
Many thanks and best regards,
Torvald

```html
<!DOCTYPE html>
<html lang="en">
<head>
<meta charset="utf-8">
<title>Vandrel background – workhaven.ch</title>
<link rel="stylesheet" href="https://fonts.googleapis.com/css2?family=Arimo&family=PT+Sans:wght@400;700&display=swap">
<style>
  :root {
    --bg-top: #e6e6e6;
    --bg-mid: #d4d4d4;
    --bg-bottom: #3c3c3c;
    --band: #2f8ad0;
    --band-light: #9fc9ea;
    --capsule: #ffffff;
    --nav-text: #666a70;
    --capsule-text: #7c8590;
    --brand-blue: #1c6fb3;
    --brand-grey: #5c5c5c;
    --accent-green: #8cc63f;
    --button-top: #1b8be0;
    --button-bottom: #0a5fa8;
    --button-edge: #0a4a85;
    --button-label: #b7ee3a;
    --white: #ffffff;
  }
  * { box-sizing: border-box; margin: 0; padding: 0; }
  html, body { width: 1200px; height: 963px; overflow: hidden; }
  body {
    position: relative;
    font-family: "PT Sans", sans-serif;
    background: linear-gradient(to bottom, var(--bg-top) 0%, var(--bg-top) 30%, var(--bg-mid) 70%, var(--bg-bottom) 100%);
  }
  .band {
    position: absolute; left: 0; top: 229px; width: 1200px; height: 30px;
    background: var(--band);
  }
  .band-left {
    position: absolute; left: 0; top: 229px; width: 243px; height: 30px;
    background: linear-gradient(to bottom, #3a8fd2, var(--band-light));
  }
  .brand {
    position: absolute; left: 16px; top: 60px;
  }
  .brand-name {
    display: flex; align-items: center; gap: 6px;
    font-size: 32px; font-weight: 700; color: var(--brand-blue); line-height: 1;
  }
  .brand-mark { width: 12px; height: 12px; border-radius: 50%; background: var(--brand-blue); }
  .brand-tagline {
    margin-top: 8px; padding-left: 16px;
    font-size: 15.5px; letter-spacing: 1px; color: var(--brand-grey);
  }
  .hero-photo {
    position: absolute; left: 0; top: 245px; width: 241px; height: 114px;
    background: linear-gradient(to bottom, #c9d6e2 0%, #8fa9c4 50%, #3f74ad 100%);
  }
  .hero-tagline {
    position: absolute; left: 15px; top: 364px; font-size: 11.5px; color: var(--brand-grey);
  }
  .hero-tagline strong { color: var(--accent-green); font-size: 14px; font-weight: 700; }
  .hero-reflection {
    position: absolute; left: 30px; top: 380px; font-size: 11px; color: var(--brand-grey); opacity: .12;
  }
  .actions { position: absolute; left: 0; top: 401px; width: 241px; }
  .action {
    display: flex; align-items: center; height: 75px; margin-bottom: 3px;
    background: linear-gradient(to bottom, var(--button-top), var(--button-bottom));
    border-bottom: 2px solid var(--button-edge);
    color: var(--white); text-decoration: none;
  }
  .action svg { width: 44px; height: 44px; margin: 0 10px 0 14px; flex: none; }
  .action-kicker { display: block; color: var(--button-label); font-size: 14px; line-height: 1.1; }
  .action-title { display: block; font-size: 20px; line-height: 1.1; }
  .site-name {
    position: absolute; left: 246px; top: 10px;
    font-size: 32px; font-weight: 700; color: #6cc9ea;
  }
  .nav {
    position: absolute; left: 648px; top: 12px; width: 329px; height: 30px;
    background: #f8f8f8; border-radius: 6px;
    display: flex; align-items: center; justify-content: center; gap: 10px;
  }
  .nav a { font-size: 13.5px; color: var(--nav-text); text-decoration: none; }
  .capsule {
    position: absolute; left: 243px; top: 65px; width: 734px; height: 824px;
    background: var(--capsule); border-radius: 6px;
  }
  .capsule-notch { position: absolute; left: 268px; top: 55px; }
  .capsule-note {
    position: absolute; left: 77px; top: 126px;
    font-family: "Arimo", sans-serif; font-size: 23px; line-height: 28px;
    color: var(--capsule-text); letter-spacing: -.3px;
  }
</style>
</head>
<body>
  <div class="band"></div>
  <div class="band-left"></div>

  <header class="brand">
    <div class="brand-name"><span class="brand-mark"></span>workhaven.ch</div>
    <div class="brand-tagline">Job Network Switzerland</div>
  </header>

  <div class="hero-photo" role="img" aria-label="Group of professionals from different careers"></div>
  <p class="hero-tagline">TAKE THE <strong>NEXT STEP</strong> IN YOUR CAREER</p>
  <p class="hero-reflection">TAKE THE NEXT STEP IN YOUR CAREER</p>

  <nav class="actions">
    <a class="action" href="#">
      <svg viewBox="0 0 44 44"><rect x="3" y="14" width="34" height="22" rx="2" fill="#f2f2f2"/><path d="M3 14 L20 27 L37 14" fill="none" stroke="#aab" stroke-width="1.5"/><circle cx="33" cy="11" r="8" fill="#3db34a"/><rect x="32" y="6" width="2" height="7" fill="#fff"/><rect x="32" y="14" width="2" height="2" fill="#fff"/></svg>
      <span><span class="action-kicker">JobNote</span><span class="action-title">Alert Service</span></span>
    </a>
    <a class="action" href="#">
      <svg viewBox="0 0 44 44"><rect x="10" y="5" width="24" height="34" fill="#f2f2f2" transform="rotate(-6 22 22)"/><g stroke="#bbb" stroke-width="1"><line x1="15" y1="14" x2="29" y2="13"/><line x1="15" y1="19" x2="30" y2="18"/><line x1="16" y1="24" x2="30" y2="23"/><line x1="16" y1="29" x2="31" y2="28"/></g></svg>
      <span><span class="action-kicker">Employers</span><span class="action-title">Post your Job</span></span>
    </a>
    <a class="action" href="#">
      <svg viewBox="0 0 44 44"><rect x="9" y="4" width="24" height="34" fill="#f2f2f2" transform="rotate(-8 21 21)"/><line x1="38" y1="18" x2="20" y2="40" stroke="#c8c8c8" stroke-width="3"/></svg>
      <span><span class="action-kicker">Job Seekers</span><span class="action-title">Post your Resume</span></span>
    </a>
  </nav>

  <div class="site-name">vandrel</div>
  <nav class="nav">
    <a href="#">Home</a><a href="#">Profile</a><a href="#">Find People</a><a href="#">Settings</a><a href="#">Help</a><a href="#">Sign out</a>
  </nav>

  <svg class="capsule-notch" width="18" height="11" viewBox="0 0 18 11"><path d="M0 11 L9 1 L18 11 Z" fill="#ffffff"/></svg>
  <main class="capsule">
    <p class="capsule-note">This is the size of the vandrel capsule. It can go as long as possible.<br>Top height and width side to side are key.<br>This auto centers as part of vandrels styling.</p>
  </main>
</body>
</html>
```